Kainoa's Luau CD cover design

I want to design the CD cover for a show. The title of the DVD is Elder Tavita Lemalo "Rise and Roam". You can see the reference of the old cd cover. At this time, we would like to make it look more classic design.
You can also based on the image 4158 of him to design.
The CD should have the information and stories inside also similar to the scan.

Colors
ec1f27

Requirements
Must have
• Just update the picture of the coconut tree that we have taken for you guys to design. Please crop the 4471 picture close the root of the coconut tree.
Nice to have
• the beach

```html
<!DOCTYPE html>
<html lang="en">
<head>
<meta charset="utf-8">
<title>Elder Tavita Lemalo – Rise and Roam CD Cover</title>
<link rel="stylesheet" href="https://fonts.googleapis.com/css2?family=Rye&family=Cinzel:wght@700&family=Oswald:wght@500&display=swap">
<style>
  :root {
    --brand-red: #ec1f27;
    --flame-core: #fff6d6;
    --flame-mid: #ffb81c;
    --flame-edge: #d9410f;
    --flame-dark: #5a1206;
    --sky-top: #c9561c;
    --sky-mid: #f08a1e;
    --sun-glow: #ffd54a;
    --sea-top: #3a4f5c;
    --sea-bottom: #1c2a33;
    --portrait-warm: #6b3a24;
    --portrait-leaf: #3f5a2a;
    --track-ink: #f4efe6;
    --spine-ink: #ffffff;
  }
  * { margin: 0; padding: 0; box-sizing: border-box; }
  html, body { width: 1200px; height: 602px; overflow: hidden; background: #ffffff; }

  .cover {
    position: relative;
    width: 1200px;
    height: 602px;
    overflow: hidden;
  }

  .scene-backdrop {
    position: absolute;
    inset: 0;
    background:
      radial-gradient(ellipse 180px 70px at 600px 415px, var(--sun-glow) 0%, rgba(255,213,74,0.55) 45%, rgba(255,213,74,0) 100%),
      linear-gradient(180deg, var(--sky-top) 0%, var(--sky-mid) 45%, #f6a52a 70%, var(--sun-glow) 73%, var(--sea-top) 74%, var(--sea-bottom) 100%);
  }

  .portrait {
    position: absolute;
    left: 620px;
    top: 45px;
    width: 580px;
    height: 557px;
    border-radius: 46% 40% 0 0 / 30% 26% 0 0;
    background:
      radial-gradient(ellipse 200px 220px at 300px 230px, #8a5234 0%, var(--portrait-warm) 60%, rgba(107,58,36,0) 100%),
      linear-gradient(180deg, #5e2a2e 0%, var(--portrait-warm) 40%, var(--portrait-leaf) 80%, #2e4420 100%);
  }

  .fire-text {
    position: absolute;
    font-family: "Rye", serif;
    color: var(--flame-core);
    line-height: 1;
    white-space: nowrap;
    -webkit-text-stroke: 1px var(--flame-edge);
    text-shadow:
      0 0 2px var(--flame-mid),
      0 -3px 4px var(--flame-mid),
      0 -6px 8px var(--brand-red),
      2px 2px 0 var(--flame-dark),
      0 0 14px rgba(217,65,15,0.8);
  }

  .back .name-first { left: 168px; top: 34px; font-size: 46px; }
  .back .name-middle { left: 99px; top: 92px; font-size: 54px; }
  .back .name-last { left: 362px; top: 66px; font-size: 40px; }
  .back .album-title { left: 99px; top: 232px; font-size: 49px; }

  .track-list {
    position: absolute;
    left: 190px;
    top: 352px;
    list-style: none;
    font-family: "Cinzel", serif;
    font-weight: 700;
    font-size: 25px;
    color: var(--track-ink);
    line-height: 43px;
    letter-spacing: 1px;
    text-shadow: 1px 1px 2px rgba(0,0,0,0.4);
  }

  .spine-label {
    position: absolute;
    left: 590px;
    font-family: "Oswald", sans-serif;
    font-weight: 500;
    font-size: 13px;
    color: var(--spine-ink);
    writing-mode: vertical-rl;
    letter-spacing: 0.5px;
    white-space: nowrap;
  }
  .spine-label.artist { top: 36px; }
  .spine-label.title { top: 452px; }

  .front .name-first { left: 738px; top: 34px; font-size: 46px; }
  .front .name-middle { left: 668px; top: 92px; font-size: 54px; }
  .front .name-last { left: 928px; top: 66px; font-size: 40px; }
  .front .album-title { left: 646px; top: 500px; font-size: 56px; }
</style>
</head>
<body>
  <main class="cover">
    <div class="scene-backdrop" role="img" aria-label="Photograph of palm tree silhouettes against an orange sunset over the ocean, trees cropped near the roots"></div>

    <section class="back">
      <div class="fire-text name-first">ELDER</div>
      <div class="fire-text name-middle">TAVITA</div>
      <div class="fire-text name-last">LEMALO</div>
      <div class="fire-text album-title">RISE AND ROAM</div>
      <ol class="track-list">
        <li>1.Title</li>
        <li>2.Title</li>
        <li>3.Title</li>
        <li>4.Sample Title</li>
        <li>5.Title</li>
      </ol>
    </section>

    <div class="spine-label artist">ELDER TAVITA LEMALO</div>
    <div class="spine-label title">RISE AND ROAM</div>

    <section class="front">
      <div class="portrait" role="img" aria-label="Photograph of the performer smiling, wearing a flower crown and a palm-leaf garland"></div>
      <div class="fire-text name-first">ELDER</div>
      <div class="fire-text name-middle">TAVITA</div>
      <div class="fire-text name-last">LEMALO</div>
      <div class="fire-text album-title">RISE AND ROAM</div>
    </section>
  </main>
</body>
</html>
```